Emergency Vehicle Installer and Security Firm Needs a Business Card

Our company "Corvalt" need a business card for our Emergency Vehicle Equipment Installation and Infrastructure Security Business. We are contract designers, manufacturers and installers for Emergency Vehicle Fleets. This includes installation of Emergency Lights, Sirens, Vehicle Graphics and Radio Communications. We also supply this products to an international market. We also do consultant, and installation of high level security access, alarm and surveillance equipment for medium to large size businesses.

The design should represent a level of trust in our professionalism and expertise. It should visually display our ongoing relationship with the emergency services, but not overtake our commitment to high level security options.

Target Market(s)

Emergency Services and Businesses requiring high level security

Industry/Entity Type

Business

Contact Information for Business Card

*note complete details will be given to the winning designer for revising. The name "Mark Pell will be used to fill in name".

Mark Pell
Managing Director
Corvalt NZ Limited
Phone: +64 027 604 91352
Email: mark.pell@corvalt-example.co.nz

Requirements
Must have
• Card must be in black. Using our logo on the top as supplied. Designers should try having the reverse side as a blurred image of police lights (red and blue) with our logo in greyscale in the centre (this is not particularly a requirement, but feel free to play around with this option).
Nice to have
• A card design that looks good when spot UV printed. A clean compact and graphic design. A grey scale feel on the front (excluding logo, but you can play around with that idea). Rounded smooth text.
Should not have
• Will update this section as designs come through - feel free to submit what you feel would look good.

```html
<!DOCTYPE html>
<html lang="en">
<head>
<meta charset="utf-8">
<title>Corvalt Business Cards</title>
<link rel="stylesheet" href="https://fonts.googleapis.com/css2?family=Open+Sans:wght@400;600;700;800&display=swap">
<style>
  :root {
    --page-bg: #2f2c2b;
    --card-dark: #3d3d3f;
    --band-grey: #555557;
    --band-dark: #3c3c3e;
    --signal-red: #e64b33;
    --name-red: #ea4a30;
    --text-white: #ffffff;
    --text-light: #d9d9d9;
    --text-muted: #a3a3a5;
  }
  * { box-sizing: border-box; margin: 0; padding: 0; }
  html, body {
    width: 1200px; height: 598px; overflow: hidden;
    background: var(--page-bg);
    font-family: "Open Sans", Arial, sans-serif;
  }
  .sheet { position: relative; width: 1200px; height: 598px; }

  .card { position: absolute; overflow: hidden; }
  .card--dark { background: var(--card-dark); }
  .card--red { background: var(--signal-red); }

  .front-dark { left: 106px; top: 54px; width: 387px; height: 218px; }
  .front-red  { left: 106px; top: 326px; width: 387px; height: 216px; }
  .back-dark  { left: 714px; top: 53px; width: 390px; height: 216px; }
  .back-red   { left: 715px; top: 325px; width: 388px; height: 214px; }

  .band { position: absolute; left: 0; right: 0; }
  .band--grey { background: var(--band-grey); }
  .band--dark { background: var(--band-dark); }
  .front-red .band { top: 68px; height: 86px; }
  .back-dark .band { top: 59px; height: 96px; }
  .back-red .band  { top: 67px; height: 86px; }

  .wordmark {
    font-weight: 800; color: var(--text-white);
    letter-spacing: 0.5px; line-height: 1; white-space: nowrap;
  }
  .wordmark--large {
    position: absolute; left: 0; right: 0; text-align: center;
    font-size: 38px;
  }
  .front-dark .wordmark--large { top: 88px; }
  .front-red .wordmark--large { top: 24px; }
  .wordmark--small {
    position: absolute; left: 32px; font-size: 19px;
  }
  .back-dark .wordmark--small { top: 38px; }
  .back-red .wordmark--small { top: 33px; left: 0; }

  .identity { position: absolute; left: 158px; }
  .back-dark .identity { top: 28px; }
  .back-red .identity { top: 24px; left: 139px; }
  .identity .name { color: var(--name-red); font-size: 13px; font-weight: 400; line-height: 16px; }
  .identity .role { color: var(--text-light); font-size: 7.5px; line-height: 14px; margin-top: 3px; }
  .identity .company { color: var(--text-muted); font-size: 7.5px; line-height: 14px; margin-top: 2px; }

  .contact { position: absolute; list-style: none; }
  .back-dark .contact { left: 248px; top: 29px; }
  .back-red .contact { left: 226px; top: 25px; }
  .contact li {
    display: flex; align-items: center; gap: 5px;
    color: var(--text-light); font-size: 7.5px; line-height: 10px;
    height: 16.5px; white-space: nowrap;
  }
  .contact svg { width: 8px; height: 8px; flex: none; fill: var(--signal-red); }
</style>
</head>
<body>
<main class="sheet">

  <section class="card card--dark front-dark" aria-label="Card front, dark">
    <div class="wordmark wordmark--large">CORVALT</div>
  </section>

  <section class="card card--red front-red" aria-label="Card front, red">
    <div class="band band--dark">
      <div class="wordmark wordmark--large">CORVALT</div>
    </div>
  </section>

  <section class="card card--dark back-dark" aria-label="Card back, dark">
    <div class="band band--grey">
      <div class="wordmark wordmark--small">CORVALT</div>
      <div class="identity">
        <p class="name">Mark Pell</p>
        <p class="role">Managing Director</p>
        <p class="company">Corvalt NZ Limited</p>
      </div>
      <ul class="contact">
        <li><svg viewBox="0 0 8 8"><rect x="2" y="0" width="4" height="8" rx="0.8"/></svg>+64 027 604 91352</li>
        <li><svg viewBox="0 0 8 8"><rect x="0" y="1.5" width="8" height="5" rx="0.6"/></svg>mark.pell@corvalt-example.co.nz</li>
        <li><svg viewBox="0 0 8 8"><circle cx="4" cy="4" r="4"/></svg>corvalt-example.co.nz</li>
      </ul>
    </div>
  </section>

  <section class="card card--red back-red" aria-label="Card back, red">
    <div class="band band--dark">
      <div class="wordmark wordmark--small" style="left:20px">CORVALT</div>
      <div class="identity">
        <p class="name">Mark Pell</p>
        <p class="role">Managing Director</p>
        <p class="company">Corvalt NZ Limited</p>
      </div>
      <ul class="contact">
        <li><svg viewBox="0 0 8 8"><rect x="2" y="0" width="4" height="8" rx="0.8"/></svg>+64 027 604 91352</li>
        <li><svg viewBox="0 0 8 8"><rect x="0" y="1.5" width="8" height="5" rx="0.6"/></svg>mark.pell@corvalt-example.co.nz</li>
        <li><svg viewBox="0 0 8 8"><circle cx="4" cy="4" r="4"/></svg>corvalt-example.co.nz</li>
      </ul>
    </div>
  </section>

</main>
</body>
</html>
```